Korvane Sky Works, LLC - Business Card

I currently have a drone business that specializes in aerial photography, thermal image inspections, deer recovery, search and rescue, custom agricultural applications. i will attach my current business card as well as some logos to incorporate for a new up to date business card
Updates

Designs look the same

Sick

Target Market(s)

farmers, hunters

Contact Information for Business Card

name address phone number (as existing card i attached)

Requirements
Must have
• im good with existing business card, but would like an agricultural twist

```html
<!DOCTYPE html>
<html lang="en">
<head>
<meta charset="utf-8">
<title>Korvane Sky Works, LLC – Business Card</title>
<link href="https://fonts.googleapis.com/css2?family=Roboto:wght@400;500;700&display=swap" rel="stylesheet">
<style>
  :root {
    --page-bg: #ececec;
    --card-bg: #ffffff;
    --brand-green: #3f8f1f;
    --brand-green-light: #5fa83b;
    --ink-dark: #1d1d1d;
    --ink-grey: #7a7a7a;
    --rule-grey: #9a9a9a;
  }
  * { box-sizing: border-box; margin: 0; padding: 0; }
  html, body {
    width: 1200px; height: 900px; overflow: hidden;
    background: var(--page-bg);
    font-family: "Roboto", Arial, sans-serif;
  }
  .sheet {
    width: 1200px; height: 900px;
    display: flex; flex-direction: column; align-items: center; justify-content: center;
    gap: 50px;
  }
  .card {
    position: relative;
    width: 630px; height: 360px;
    background: var(--card-bg);
    border-radius: 22px;
    overflow: hidden;
    box-shadow: 0 6px 18px rgba(0,0,0,0.18);
  }
  /* front */
  .card-front .swoosh { position: absolute; left: 0; bottom: 0; width: 630px; height: 360px; }
  .brand-mark {
    position: absolute; left: 46px; top: 88px; width: 200px;
    display: flex; flex-direction: column; align-items: center; gap: 10px;
  }
  .brand-dot {
    width: 22px; height: 22px; border-radius: 50%;
    background: var(--brand-green);
  }
  .brand-name {
    font-weight: 700; font-size: 34px; color: var(--brand-green);
    letter-spacing: 0.5px; text-align: center; line-height: 1.05;
  }
  .divider {
    position: absolute; left: 276px; top: 40px; width: 1px; height: 180px;
    background: var(--rule-grey);
  }
  .contact { position: absolute; left: 300px; top: 42px; color: var(--ink-grey); }
  .contact .person-name {
    font-weight: 700; font-size: 25px; color: var(--brand-green); letter-spacing: 0.3px;
  }
  .contact .person-role { font-size: 18px; margin-top: 2px; }
  .contact .address { font-size: 18px; margin-top: 14px; line-height: 1.35; }
  .contact-list { list-style: none; margin-top: 12px; font-size: 18px; line-height: 1.45; }
  .contact-list li { display: flex; align-items: center; gap: 8px; }
  .contact-list svg { width: 15px; height: 15px; flex: none; }
  .web-accent { color: var(--brand-green); }
  /* back */
  .card-back .brand-mark { left: 215px; top: 70px; }
  .services {
    position: absolute; left: 0; right: 0; top: 210px;
    text-align: center; font-size: 21px; color: var(--ink-dark); line-height: 1.5;
  }
  .services .bullet { color: var(--brand-green); margin: 0 6px 0 14px; }
  .services .bullet:first-child { margin-left: 0; }
</style>
</head>
<body>
<main class="sheet">

  <section class="card card-front" aria-label="Business card front">
    <svg class="swoosh" viewBox="0 0 630 360" aria-hidden="true">
      <path d="M0 250 C 180 290, 400 330, 630 360 L 0 360 Z" fill="#1d1d1d"/>
      <path d="M0 262 C 190 300, 410 338, 630 362 L 0 362 Z" fill="var(--brand-green)"/>
      <path d="M0 300 C 200 330, 420 350, 630 362 L 0 362 Z" fill="var(--brand-green-light)" opacity="0.6"/>
    </svg>

    <div class="brand-mark">
      <span class="brand-dot"></span>
      <span class="brand-name">Korvane</span>
    </div>

    <span class="divider"></span>

    <div class="contact">
      <p class="person-name">MASON REEDE</p>
      <p class="person-role">Owner</p>
      <p class="address">214 W. Orchard St.<br>Ferrin, OH 45890</p>
      <ul class="contact-list">
        <li>
          <svg viewBox="0 0 16 16"><path fill="var(--ink-dark)" d="M3.6 1.5l2.2 2.6-1.3 1.6c.9 2 2.4 3.5 4.4 4.4l1.6-1.3 2.6 2.2-1.4 2.5C6.6 13.2 2.8 9.4 1.3 2.9z"/></svg>
          419-555-0182
        </li>
        <li>
          <svg viewBox="0 0 16 16"><rect x="1.5" y="3.5" width="13" height="9" rx="1" fill="none" stroke="var(--ink-dark)" stroke-width="1.6"/><path d="M2 4l6 5 6-5" fill="none" stroke="var(--ink-dark)" stroke-width="1.6"/></svg>
          hello@korvaneskyworks.com
        </li>
        <li>
          <svg viewBox="0 0 16 16"><circle cx="8" cy="8" r="6.5" fill="var(--brand-green)"/><path d="M1.5 8h13M8 1.5c-3 3-3 10 0 13M8 1.5c3 3 3 10 0 13" fill="none" stroke="#fff" stroke-width="1"/></svg>
          <span>www.<span class="web-accent">korvaneskyworks</span>.com</span>
        </li>
      </ul>
    </div>
  </section>

  <section class="card card-back" aria-label="Business card back">
    <div class="brand-mark">
      <span class="brand-dot"></span>
      <span class="brand-name">Korvane</span>
    </div>
    <p class="services">
      <span class="bullet">●</span>Thermal Image Inspections<span class="bullet">●</span>Deer Recovery<br>
      <span class="bullet">●</span>Search &amp; Rescue<span class="bullet">●</span>Real Estate Photography
    </p>
  </section>

</main>
</body>
</html>
```